Business Card Design

Personal training company in the fitness industry

Industry/Entity Type

Training

Contact Information for Business Card

(Front of card)
Peak Hour Fitness
417 Wexley Road Brackenvale 6172 (Inside IronHaus365 complex)
Dario Halvorsen
Personal Trainer
halvdario@mailora.net
0412 903 548
Back of card
One on One Training
Group Training (min 3)
Outdoor bootcamps
Workout programs
Meal guides
Competition preparation
(bottom middle of card)
GET TO YOUR PEAK!

```html
<!DOCTYPE html>
<html lang="en">
<head>
<meta charset="utf-8">
<title>Peak Hour Fitness – Business Card</title>
<link rel="stylesheet" href="https://fonts.googleapis.com/css2?family=Exo+2:wght@400;500&display=swap">
<style>
  :root {
    --backdrop: #4a4a4a;
    --card: #050505;
    --ink: #f2f2f2;
    --ink-soft: #d6d6d6;
    --metal: #a9a9a9;
    --mark: #8f8f8f;
    --rule: #3a3a3a;
  }
  * { margin: 0; padding: 0; box-sizing: border-box; }
  html, body { width: 1200px; height: 1000px; overflow: hidden; }
  body {
    background: var(--backdrop);
    font-family: "Exo 2", sans-serif;
    position: relative;
  }
  .card {
    position: absolute;
    left: 235px;
    width: 725px;
    height: 432px;
    background: var(--card);
    box-shadow: 0 6px 18px rgba(0,0,0,.45);
  }
  .card--front { top: 46px; }
  .card--back { top: 523px; }

  .brand {
    position: absolute;
    text-align: center;
    color: var(--metal);
    font-weight: 500;
  }
  .brand__dot {
    display: block;
    margin: 0 auto 22px;
    width: 124px;
    height: 124px;
    border-radius: 50%;
    background: var(--mark);
  }
  .brand__name { display: block; font-size: 42px; line-height: 1; letter-spacing: 3px; }
  .brand__sub { display: block; font-size: 20px; letter-spacing: 10px; margin-top: 6px; padding-left: 10px; }

  .card--front .brand { left: 0; width: 385px; top: 104px; }
  .divider {
    position: absolute;
    left: 385px; top: 104px;
    width: 1px; height: 226px;
    background: var(--rule);
  }
  .contact { position: absolute; left: 405px; top: 124px; color: var(--ink); }
  .contact__name { font-size: 21px; font-weight: 500; letter-spacing: 1.5px; line-height: 1.2; }
  .contact__role { font-size: 15.5px; color: var(--ink-soft); line-height: 1.3; letter-spacing: 1px; }
  .contact__lines { margin-top: 18px; font-size: 16px; line-height: 20px; letter-spacing: 1.1px; }
  .contact__line { display: flex; align-items: center; gap: 6px; }
  .contact__line svg { width: 14px; height: 12px; fill: var(--ink); }
  .contact__address { margin-top: 16px; font-size: 16px; line-height: 19px; letter-spacing: 1.1px; }

  .card--back .brand { left: 0; width: 725px; top: 46px; }
  .services {
    position: absolute; left: 0; width: 725px; top: 298px;
    text-align: center; color: var(--ink); font-size: 16px; line-height: 19px;
    letter-spacing: 1.2px;
  }
  .slogan {
    position: absolute; left: 0; width: 725px; top: 353px;
    text-align: center; color: var(--metal); font-size: 20px; letter-spacing: 2.5px;
  }
</style>
</head>
<body>
  <section class="card card--front">
    <div class="brand">
      <span class="brand__dot"></span>
      <span class="brand__name">PEAK HOUR</span>
      <span class="brand__sub">FITNESS</span>
    </div>
    <div class="divider"></div>
    <div class="contact">
      <p class="contact__name">Dario Halvorsen</p>
      <p class="contact__role">Personal Trainer</p>
      <div class="contact__lines">
        <p class="contact__line">
          <svg viewBox="0 0 14 12" aria-hidden="true"><path d="M3 1 L5 3.5 L4 5 Q5.5 7.5 8 8.5 L9.5 7.5 L12 9.5 L10.5 11.5 Q5 11 2 6 Q1 3 3 1 Z"/></svg>
          0412 903 548
        </p>
        <p class="contact__line">
          <svg viewBox="0 0 14 12" aria-hidden="true"><path d="M1 2 H13 V11 H1 Z M2 3 V3.6 L7 7 L12 3.6 V3 Z" fill-rule="evenodd"/></svg>
          halvdario@mailora.net
        </p>
      </div>
      <p class="contact__address">417 Wexley Road<br>Brackenvale 6172<br>(Inside IronHaus365 complex)</p>
    </div>
  </section>

  <section class="card card--back">
    <div class="brand">
      <span class="brand__dot"></span>
      <span class="brand__name">PEAK HOUR</span>
      <span class="brand__sub">FITNESS</span>
    </div>
    <p class="services">One on One Training Group - Training (min 3) Outdoor bootcamps<br>WorKout programs - Meal guides - Competition preparation</p>
    <p class="slogan">GET TO YOUR PEAK!</p>
  </section>
</body>
</html>
```